Dryer Vent Cleaning Postcard Design

We need a postcard design for Flue Wranglers, a company that specializes in dryer vent cleaning, repairs and upgrades. Dryer vents need periodic cleaning to avoid lint clogging, dryer malfunction, long dry times and even a house fire. This card will be sent to residential and businesses prospects to introduce them to our services and the importance of maintaining their dryer vents. Our website is @ fluewrangling.com and provides information about our services, photos of our work and our general color scheme (purple/orange). Final print size will be 5x7 horizontal.

Target Market(s)

homeowners and business owners (spas, salons, grooming, gyms, laundrymats, etc)

Requirements
Must have
• Reduce the risk of fire
shortened dry times
lower energy consumption
18000 dryer fires caused in the US per year
Nice to have
• Does your dryer take too long to dry?

```html
<!DOCTYPE html>
<html lang="en">
<head>
<meta charset="utf-8">
<title>Flue Wranglers – Dryer Vent Cleaning Postcard</title>
<link rel="stylesheet" href="https://fonts.googleapis.com/css2?family=Figtree:wght@400;500;600;700&display=swap">
<style>
  :root {
    --purple: #433a6e;
    --orange: #f47f4a;
    --orange-deep: #e0703f;
    --ink: #111111;
    --white: #ffffff;
    --dryer: #d7d2cf;
    --dryer-shade: #a9a3a0;
    --uniform: #b39a80;
    --edge: #d4d4d4;
  }
  * { box-sizing: border-box; margin: 0; padding: 0; }
  html, body {
    width: 816px; height: 1200px; overflow: hidden;
    background: var(--white);
    font-family: "Figtree", "Helvetica Neue", Arial, sans-serif;
  }
  .postcard {
    position: absolute; left: 61px; width: 694px; height: 496px;
    background: var(--white); overflow: hidden;
    box-shadow: 0 0 0 1px var(--edge), 0 1px 3px rgba(0,0,0,.12);
  }
  .postcard--front { top: 88px; }
  .postcard--back { top: 617px; }
  .backdrop { position: absolute; inset: 0; width: 694px; height: 496px; }

  /* front */
  .brand-mark {
    position: absolute; left: 30px; top: 60px; width: 220px; height: 110px;
    display: flex; align-items: center; justify-content: center; gap: 10px;
  }
  .brand-mark__dot { width: 30px; height: 30px; border-radius: 50%; background: var(--orange); flex: none; }
  .brand-mark__name { font-size: 26px; font-weight: 700; color: var(--white); letter-spacing: .5px; }
  .art-dryer {
    position: absolute; left: 94px; top: 212px; width: 232px; height: 252px;
    border-radius: 6px;
    background: linear-gradient(160deg, #4a4a4a 0%, #4a4a4a 22%, var(--dryer) 30%, var(--dryer-shade) 100%);
  }
  .front-copy { position: absolute; right: 40px; top: 20px; text-align: right; }
  .headline {
    color: var(--purple); font-size: 63px; font-weight: 600; line-height: 61px; letter-spacing: -0.5px;
  }
  .tagline {
    margin-top: 16px; color: var(--orange); font-size: 24px; font-weight: 600; line-height: 29px;
  }
  .tagline-rule { display: block; margin: 12px 0 0 auto; width: 54px; height: 4px; background: var(--purple); }
  .question {
    margin-top: 30px; color: var(--ink); font-size: 28px; font-weight: 700; line-height: 34px;
  }
  .call {
    margin-top: 22px; color: var(--purple); font-size: 27px; font-weight: 700; line-height: 32px;
  }
  .call__number { color: var(--orange); }
  .contact { color: var(--ink); font-size: 18.5px; font-weight: 500; line-height: 26px; margin-top: 4px; }
  .contact li { list-style: none; display: flex; justify-content: flex-end; align-items: center; gap: 8px; }
  .contact svg { width: 18px; height: 18px; }
  .contact b { font-weight: 700; }

  /* back */
  .intro {
    position: absolute; left: 39px; top: 34px; width: 278px;
    color: var(--white); font-size: 15.8px; line-height: 19.8px; font-weight: 400;
    letter-spacing: -0.1px;
  }
  .intro-rule { position: absolute; left: 39px; top: 208px; width: 55px; height: 4px; background: var(--orange); }
  .benefits { position: absolute; left: 40px; top: 262px; width: 280px; list-style: none; }
  .benefit {
    display: flex; align-items: flex-start; gap: 12px;
    color: var(--white); font-size: 19px; line-height: 23px; margin-bottom: 15px;
    white-space: nowrap;
  }
  .benefit svg { width: 33px; height: 33px; flex: none; margin-top: -5px; }
  .stamp-box {
    position: absolute; left: 586px; top: 23px; width: 85px; height: 84px;
    border: 1.5px solid #8a8a8a;
  }
  .art-technician {
    position: absolute; left: 326px; top: 162px; width: 104px; height: 276px;
    border-radius: 30px 30px 8px 8px;
    background: linear-gradient(180deg, #8f4a3a 0%, var(--uniform) 18%, #a88d73 100%);
  }
  .follow {
    position: absolute; left: 0; right: 0; top: 460px;
    display: flex; justify-content: center; align-items: center; gap: 8px;
    color: var(--white); font-size: 13px;
  }
  .follow__dot { width: 12px; height: 12px; border-radius: 50%; background: var(--white); }
  .follow__handle { font-weight: 700; }
</style>
</head>
<body>

<section class="postcard postcard--front">
  <svg class="backdrop" viewBox="0 0 694 496" aria-hidden="true">
    <path d="M0,0 H15 C60,150 140,320 300,430 C420,480 560,465 694,432 V496 H0 Z" fill="var(--purple)"/>
    <path d="M0,377 C150,440 340,470 490,474 C590,476 650,462 694,441 V496 H0 Z" fill="var(--orange-deep)"/>
    <path d="M0,413 C160,460 360,482 500,482 C600,481 650,470 694,458 V496 H0 Z" fill="var(--orange)"/>
  </svg>

  <div class="brand-mark">
    <span class="brand-mark__dot"></span>
    <span class="brand-mark__name">Flue Wranglers</span>
  </div>

  <div class="art-dryer" role="img" aria-label="Illustration of a dryer with lint bursting out of its top"></div>

  <div class="front-copy">
    <h1 class="headline">Dryer Vent<br>Cleaning</h1>
    <p class="tagline">Your Professional Dryer Vent<br>Cleaning Solution</p>
    <span class="tagline-rule"></span>
    <p class="question">Does your dryer<br>take too long to dry?</p>
    <p class="call">Call Now! <span class="call__number">555-014-2270</span></p>
    <ul class="contact">
      <li>
        <svg viewBox="0 0 18 18" aria-hidden="true"><rect x="1" y="4" width="16" height="11" fill="#6c8fd6"/><path d="M1,4 L9,10 L17,4" fill="none" stroke="#fff" stroke-width="1.4"/></svg>
        office@fluewrangling.com
      </li>
      <li>
        <svg viewBox="0 0 18 18" aria-hidden="true"><g fill="none" stroke="#6c8fd6" stroke-width="1.4"><circle cx="9" cy="9" r="7.5"/><ellipse cx="9" cy="9" rx="3.2" ry="7.5"/><path d="M1.5,9 H16.5 M3,5 H15 M3,13 H15"/></g></svg>
        <span>www.<b>fluewrangling</b>.com</span>
      </li>
    </ul>
  </div>
</section>

<section class="postcard postcard--back">
  <svg class="backdrop" viewBox="0 0 694 496" aria-hidden="true">
    <path d="M0,0 H351 C340,160 390,320 500,444 L500,496 H0 Z" fill="var(--purple)"/>
    <path d="M0,469 C200,435 500,435 694,469 V496 H0 Z" fill="var(--orange-deep)"/>
    <path d="M0,496 C200,452 500,452 694,486 V496 Z" fill="var(--orange)"/>
  </svg>

  <p class="intro">Our process is simple, our technicians are super nice and our services are affordable. We carry the equipment, material, and knowledge to clean or repair any dryer vent issue. Our work is guaranteed and we are fully insured. Call the local guys at Flue Wranglers to solve your dryer vent issues.</p>
  <span class="intro-rule"></span>

  <ul class="benefits">
    <li class="benefit">
      <svg viewBox="0 0 32 32" aria-hidden="true"><path d="M16,3 C18,9 26,13 26,21 A10,10 0 0 1 6,21 C6,15 10,12 11,8 C13,12 14,13 15,14 C16,10 16,7 16,3 Z M16,29 C12,29 12,24 16,19 C20,24 20,29 16,29 Z" fill="none" stroke="#fff" stroke-width="1.3"/></svg>
      <span>Reduce the risk of fire</span>
    </li>
    <li class="benefit">
      <svg viewBox="0 0 32 32" aria-hidden="true"><g fill="none" stroke="#fff" stroke-width="1.3"><circle cx="16" cy="17" r="2.5"/><path d="M16,14.5 C12,10 14,4 16,2 C18,6 19,11 16,14.5 Z"/><path d="M18.2,18.3 C24,17 28,22 28,25 C24,25 20,23 18.2,18.3 Z"/><path d="M13.8,18.3 C12,24 6,26 3,25 C5,21 9,18 13.8,18.3 Z"/></g></svg>
      <span>Shortened dry times</span>
    </li>
    <li class="benefit">
      <svg viewBox="0 0 32 32" aria-hidden="true"><g fill="none" stroke="#fff" stroke-width="1.3"><circle cx="16" cy="16" r="10"/><path d="M16,2 V6 M16,26 V30 M2,16 H6 M26,16 H30 M6,6 L9,9 M23,23 L26,26 M26,6 L23,9 M9,23 L6,26"/><path d="M17,9 L12,17 H16 L15,23 L20,15 H16 Z"/></g></svg>
      <span>Lower energy consumption</span>
    </li>
    <li class="benefit">
      <svg viewBox="0 0 32 32" aria-hidden="true"><g fill="none" stroke="#fff" stroke-width="1.3"><rect x="5" y="3" width="22" height="27"/><path d="M5,8 H27"/><circle cx="16" cy="19" r="7"/><circle cx="16" cy="19" r="4.5"/><circle cx="19" cy="5.5" r="1"/><circle cx="23" cy="5.5" r="1"/><path d="M8,5.5 H14"/></g></svg>
      <span>18000 dryer fires caused in<br>the US per year</span>
    </li>
  </ul>

  <div class="stamp-box" aria-label="Postage stamp area"></div>

  <div class="art-technician" role="img" aria-label="Illustration of a vent cleaning technician in a work uniform holding a vent brush on his shoulder"></div>

  <div class="follow">
    <span>Follow Us</span>
    <span class="follow__dot"></span>
    <span class="follow__handle">@FlueWranglers</span>
  </div>
</section>

</body>
</html>
```